Velmora Outcomes Brochure Design Project

- Who we are?
Velmora Outcomes is New Internet Marketing Company Based in China.

It is our aim to provide Chinese clients with the means to internationally market their product, via the Internet.

Our primary products are Outsourced Design ( Thanks to Pixel hive and the amazing designers who use it), SEO and Virtual Hosting.

- Project Brief
Design a vibrant and fresh brochure that introduces the fundamentals of SEO. There is no restriction to the number of pages, however all the info I have included in this brief must be included.

- Colour Palette
Please see link or download the Adobe Swatch Exchange File or follow the link below
http://tintaro.example.com/#themes/search?term=5830716
Updates

Logo updated - grey background removed

Various file formats added for logo and brochure content

Brochure zip file add containing logo in different formats.

Adobe color scheme file added

The general corporate colors are:

Base Color: CMYK :0, 60, 80, 0  Hex: FF6633
Dark Orange: CMYK: 0, 72, 96, 30 Hex: B23308
Light Orange: CMYK 0, 42, 56, 0 Hex: FF9571
Grey: CMYK 0, 0, 0, 48 Hex: 858585
Light Grey: CMYK 0, 0, 0, 26 Hex: BDBDBD

Please note that I'm happy for other colors to be included, however I would like these the corporate branding colors to be clearly present through the brochure.

Hi All

First place payment has increased to $600 - Looking to see some creative designs!

Hi All

Project Deadline Extended
Reason: I have increase the budget and extend the deadline as I need to see more design.

I have attached a zip file that contains example brochures I like.

We are not keen on the table data its a little plain. We have create an info-graphic to replace one of the table and would like to see it included in the design.

Project Deadline Extended
Reason: A few designers have asked for this extension and I would like to see additional designs. Thanks Marek

Target Market(s)

- Our Target Audience is..
It is small to medium businesses looking to reach out to the international market.
Our clients still very much operate on a face to face level in business and are new to the concept of Internet marketing

However this must look professional, Marketable and Clean, with the power of connecting people globally, through SEO and design to be reflected visually in the brochure.

Industry/Entity Type

Internet

Requirements
Must have
• One or more of the FACTS that I have highlighted need to stand out on each page. These FACTS can be found the document attached to this brief and are under the section titled 'Did You Know!'. Not every fact in this section needs to be highlighted in the brochure, but each page needs to have at least, one or more fact that stands out, soemwhere on the page.
See attached document, under the heading 'Did you Know!' and use one or two of these facts to spruce up the pages!

One image/ per page or per two pages MUST be included!

- Provide stock photos and please send us a message with the additional cost of these with your submission

The Table data, that I have included in the attachment must be included in the body of the pages - BUT the table format is not necessary and you can place the information in the body like plain text.

The brochure size should be a little larger than A4.

Please design the back page, like a pocket to hold paper and other material in it that I include with this brochure.

```html
<!DOCTYPE html>
<html lang="en">
<head>
<meta charset="utf-8">
<title>Velmora Outcomes – SEO Brochure</title>
<link href="https://fonts.googleapis.com/css2?family=Open+Sans:ital,wght@0,400;0,600;0,700;0,800;1,700&display=swap" rel="stylesheet">
<style>
:root{
  --orange:#ff6633;
  --orange-dark:#b23308;
  --orange-light:#ff9571;
  --grey:#858585;
  --grey-light:#bdbdbd;
  --cell:#e6e6e6;
  --cell-alt:#d4d4d4;
  --ink:#3a3a3a;
  --black:#0d0d0d;
  --paper:#ffffff;
}
*{box-sizing:border-box;margin:0;padding:0}
html,body{width:1200px;height:2518px;overflow:hidden;background:var(--paper)}
body{position:relative;font-family:"Open Sans",Arial,sans-serif;color:var(--ink);font-size:7.4px;line-height:1.38}
.block{position:absolute}
.dark-band{background:
  repeating-linear-gradient(90deg,rgba(255,255,255,0) 0 38px,rgba(150,150,150,.28) 38px 62px,rgba(255,255,255,0) 62px 96px,rgba(90,90,90,.35) 96px 104px),
  linear-gradient(180deg,#1a1a1a 0%,#4a4a4a 45%,#111 100%)}
.brand-plate{position:absolute;background:#fff;padding:9px 16px}
.brand-plate .name{font-weight:600;font-size:16px;color:var(--ink);white-space:nowrap}
.photo{position:absolute}
.photo-seo{background:linear-gradient(135deg,#9aa4ad,#d7dde2 55%,#7d8891)}
.photo-pack{background:linear-gradient(135deg,#c6ccd2,#f0f1f2 50%,#9ea6ad)}
.photo-globe{background:radial-gradient(circle at 50% 50%,#eef3f8 0%,#b9c8d6 45%,#d9e1e9 100%)}
.photo-blog{background:linear-gradient(135deg,#6c6f73,#b5b8bb 55%,#3e4044)}
.photo-design{background:linear-gradient(135deg,#b7bcc2,#eceef0 55%,#8a9198)}
.section-tag{position:absolute;background:var(--orange);color:#fff;font-weight:700;display:flex;align-items:center;gap:10px;padding:0 16px}
.section-tag::before{content:"";flex:none;width:12px;height:12px;background:#fff}
.col p{margin-bottom:5px}
.col h3{color:var(--orange);font-size:10.5px;font-weight:700;margin:4px 0 3px}
.col h2{color:var(--ink);font-size:11px;font-weight:700;margin-bottom:2px}
.col .sub{font-size:6.5px;color:var(--grey);margin-bottom:6px}
.list-2{display:grid;grid-template-columns:1fr 1fr;margin:3px 0 6px}
.note{background:var(--orange);color:#fff;padding:5px 7px;margin:5px 0}
.note b{display:block;font-size:8px}
.note-soft{background:var(--orange-light);color:#fff;padding:5px 7px;margin:5px 0}
.fact{position:absolute;background:var(--orange);color:#fff;padding:5px 9px}
.fact .head{font-weight:700;font-style:italic;font-size:10px}
.fact .head span{color:var(--black)}
.method{width:100%;border-collapse:separate;border-spacing:0 2px;font-size:6.6px}
.method th{background:var(--orange);color:#fff;text-align:left;font-weight:600;width:36%;padding:5px 5px;vertical-align:top}
.method td{background:var(--cell);padding:5px 5px;vertical-align:top}
.method tr.tall th,.method tr.tall td{height:42px}
.pack{width:100%;border-collapse:collapse;font-size:6.6px;margin:3px 0 6px}
.pack tr:first-child td{background:var(--grey);color:#fff;font-weight:700}
.pack td{padding:1.5px 4px;background:var(--cell)}
.pack tr:nth-child(even) td{background:var(--cell-alt)}
.pack td:last-child{text-align:right}
.steps{list-style:none;margin:3px 0}
.steps li{margin-bottom:2px}
</style>
</head>
<body>

<section class="block dark-band" style="left:565px;top:0;width:635px;height:340px" aria-label="Front cover">
  <div class="brand-plate" style="right:18px;top:26px"><span class="name">Velmora Outcomes</span></div>
</section>

<section class="block" style="left:0;top:352px;width:1200px;height:448px" aria-label="SEO spread">
  <div class="photo photo-seo" role="img" aria-label="Photo of a search engine results screen" style="left:0;top:0;width:295px;height:205px"></div>
  <div class="section-tag" style="left:0;top:80px;width:160px;height:46px;font-size:30px">SEO</div>

  <div class="col block" style="left:305px;top:4px;width:285px">
    <p>Search engines visit more than 60 billion pages a day and sort them into their databases of pages. During this process each page is given a rank score.</p>
    <p>This ranking is based on a very complex equation containing many factors. Every time a search term is entered the engine returns the pages it judges most relevant, and the pages at the top of that list receive the largest share of visitors.</p>
    <p>Search Engine Optimisation, known as SEO, is the practice of making sure your website meets these factors, so that customers searching for your products find you first rather than your competitors.</p>
    <p>However this is not the end of it: search engines change their methods many times each year, so your position must be watched and improved on a steady basis.</p>
  </div>

  <div class="col block" style="left:140px;top:214px;width:450px">
    <h3>SEO Packages</h3>
    <p>Whether you are just starting out or are a well established business, we have an SEO package to suit both the size and the goals of your company.</p>
    <p>All of our packages include the following optimisation activities. This is not a one time task: each is repeated and reviewed every month.</p>
    <div class="list-2">
      <div>Website Audit<br>Competitor Analysis<br>Keyword Research<br>Website Structure<br>XML Validation<br>Off-Site Optimisation<br>Meta Tag Optimisation</div>
      <div>Content Optimisation<br>Image Optimisation<br>Internal Optimisation<br>Robots.txt Improvements<br>Link Building Reports<br>Webmaster Tools</div>
    </div>
    <p>If you are serious about being found, our team will build a plan that grows your visibility month by month in every market you wish to reach.</p>
  </div>
  <div class="fact" style="left:140px;top:400px;width:450px;height:38px">
    <div class="head">Did you know .....<span>!</span></div>
    <div>Over 90% of users never click past the first page of search results, so your ranking truly matters.</div>
  </div>

  <div class="col block" style="left:615px;top:4px;width:280px">
    <h2>Our Method Vs The Traditional Method</h2>
    <div class="sub">See for yourself</div>
    <h3>Our Method</h3>
    <table class="method">
      <tr class="tall"><th>Cost</th><td>Low cost. Paid monthly with no large upfront payment, and each plan may be changed as you grow.</td></tr>
      <tr class="tall"><th>Nature of Investment</th><td>Long term digital asset. Your ranking keeps bringing visitors long after the work is done.</td></tr>
      <tr class="tall"><th>Availability to business</th><td>Every day, all day. Customers can find you at any hour from any country.</td></tr>
      <tr class="tall"><th>Time required</th><td>Little of your own time. Our team handles research, changes and monthly reports for you.</td></tr>
      <tr class="tall"><th>Ability to target audience</th><td>Highly targeted. Only people searching for your products will reach your pages.</td></tr>
    </table>
  </div>
  <div class="col block" style="left:910px;top:4px;width:280px">
    <table class="method">
      <tr class="tall"><th>Change monitoring based on feedback</th><td>Results are tracked weekly and changes are made quickly using real visitor data.</td></tr>
    </table>
    <h3>Traditional Method</h3>
    <table class="method">
      <tr class="tall"><th>Cost</th><td>High cost. Print, stands and travel all require large payments before results appear.</td></tr>
      <tr class="tall"><th>Nature of Investment</th><td>Short term. Once the event or print run ends the value quickly fades away.</td></tr>
      <tr class="tall"><th>Availability to business</th><td>Limited to opening hours and to the places your staff can travel.</td></tr>
      <tr class="tall"><th>Time required</th><td>Many days of planning, meetings and travel for each campaign.</td></tr>
      <tr class="tall"><th>Ability to target audience</th><td>Broad. Messages reach many people who have no interest in your offer.</td></tr>
      <tr class="tall"><th>Change monitoring based on feedback</th><td>Slow. Feedback arrives late and changes cost extra money.</td></tr>
    </table>
  </div>
</section>

<section class="block" style="left:0;top:812px;width:1200px;height:400px" aria-label="SEO packages spread">
  <div class="photo photo-pack" role="img" aria-label="Photo of a business desk with laptop" style="left:0;top:4px;width:295px;height:150px"></div>
  <div class="section-tag" style="left:0;top:56px;width:200px;height:40px;font-size:20px">SEO Packages</div>

  <div class="col block" style="left:305px;top:4px;width:285px">
    <h3>Start-up Browse Package</h3>
    <p>Just starting up and don't have a large budget? Don't panic, our start-up package is for you. We will help optimise your website and online marketing strategy.</p>
    <table class="pack">
      <tr><td>Website Plan</td><td>3 Pages</td></tr>
      <tr><td>No. of Keywords</td><td>5</td></tr>
      <tr><td>Keywords on the first page</td><td>2</td></tr>
      <tr><td>Delivery timeframe</td><td>3 to 6 months</td></tr>
      <tr><td>Manual Directory Submission</td><td>100</td></tr>
      <tr><td>Article Submission</td><td>10</td></tr>
      <tr><td>Forum Posting</td><td>10</td></tr>
      <tr><td>Blog Commenting</td><td>10</td></tr>
      <tr><td>Blog Creation</td><td>1</td></tr>
      <tr><td>Social Bookmarking Submission</td><td>50</td></tr>
    </table>
    <h3>Small Business Silver Package</h3>
    <p>Are you an established small business and are looking to reach more customers and a wider market? Let us open the doors for you.</p>
    <table class="pack">
      <tr><td>Website Plan</td><td>5 Pages</td></tr>
      <tr><td>No. of Keywords</td><td>10</td></tr>
      <tr><td>Keywords on the first page</td><td>4</td></tr>
      <tr><td>Delivery timeframe</td><td>3 to 6 months</td></tr>
      <tr><td>Manual Directory Submission</td><td>200</td></tr>
      <tr><td>Article Submission</td><td>20</td></tr>
      <tr><td>Forum Posting</td><td>20</td></tr>
      <tr><td>Blog Commenting</td><td>20</td></tr>
      <tr><td>Social Bookmarking Submission</td><td>100</td></tr>
    </table>
  </div>

  <div class="col block" style="left:615px;top:4px;width:280px">
    <h3>Start-up Browse Package</h3>
    <p>Our start-up plan gives a new business a simple first step online, with clear monthly goals and a report showing your progress.</p>
    <table class="pack">
      <tr><td>Website Plan</td><td>3 Pages</td></tr>
      <tr><td>No. of Keywords</td><td>5</td></tr>
      <tr><td>Keywords on the first page</td><td>2</td></tr>
      <tr><td>Delivery timeframe</td><td>3 to 6 months</td></tr>
      <tr><td>Manual Directory Submission</td><td>100</td></tr>
      <tr><td>Article Submission</td><td>10</td></tr>
      <tr><td>Forum Posting</td><td>10</td></tr>
      <tr><td>Blog Commenting</td><td>10</td></tr>
      <tr><td>Social Bookmarking Submission</td><td>50</td></tr>
    </table>
    <h3>Small Business Silver Package</h3>
    <table class="pack">
      <tr><td>Website Plan</td><td>5 Pages</td></tr>
      <tr><td>No. of Keywords</td><td>10</td></tr>
      <tr><td>Keywords on the first page</td><td>4</td></tr>
      <tr><td>Delivery timeframe</td><td>3 to 6 months</td></tr>
      <tr><td>Manual Directory Submission</td><td>200</td></tr>
      <tr><td>Article Submission</td><td>20</td></tr>
      <tr><td>Forum Posting</td><td>20</td></tr>
      <tr><td>Social Bookmarking Submission</td><td>100</td></tr>
    </table>
  </div>
  <div class="col block" style="left:910px;top:4px;width:280px">
    <h3>Medium Business Gold Package</h3>
    <p>Are a well established business? Looking to improve your overall turnover or simply looking to increase traffic and visitor numbers? This plan brings steady growth.</p>
    <table class="pack">
      <tr><td>Website Plan</td><td>10 Pages</td></tr>
      <tr><td>No. of Keywords</td><td>15</td></tr>
      <tr><td>Keywords on the first page</td><td>8</td></tr>
      <tr><td>Delivery timeframe</td><td>3 months</td></tr>
      <tr><td>Manual Directory Submission</td><td>400</td></tr>
      <tr><td>Article Submission</td><td>40</td></tr>
      <tr><td>Forum Posting</td><td>40</td></tr>
      <tr><td>Blog Commenting</td><td>40</td></tr>
      <tr><td>Blog Creation</td><td>2</td></tr>
      <tr><td>Social Bookmarking Submission</td><td>150</td></tr>
    </table>
    <h3>Large Business Diamond Package</h3>
    <p>Are you already a large international company looking to further expand your international and domestic market position? Our experts can drive more visitors.</p>
    <table class="pack">
      <tr><td>Website Plan</td><td>20 Pages</td></tr>
      <tr><td>No. of Keywords</td><td>30</td></tr>
      <tr><td>Keywords on the first page</td><td>15</td></tr>
      <tr><td>Delivery timeframe</td><td>3 months</td></tr>
      <tr><td>Manual Directory Submission</td><td>800</td></tr>
      <tr><td>Article Submission</td><td>80</td></tr>
      <tr><td>Forum Posting</td><td>80</td></tr>
      <tr><td>Blog Commenting</td><td>80</td></tr>
      <tr><td>Social Bookmarking Submission</td><td>300</td></tr>
    </table>
  </div>
</section>

<section class="block" style="left:0;top:1222px;width:1200px;height:505px" aria-label="Hosting and blog spread">
  <div class="col block" style="left:10px;top:6px;width:285px">
    <h3>Cloud computing and International Hosting</h3>
    <p>Cloud computing is changing the way small business work. You no longer need to spend thousands on hardware; the host keeps your files safe and available.</p>
    <p>Our servers are located in several countries so your site loads quickly for overseas customers wherever they happen to be.</p>
    <p>Improve your international market share by choosing one of our hosting plans.</p>
    <div class="note">
      <b>Location based SEO</b>
      Search engines favour sites hosted near the searcher. A server in your target country can lift your ranking in that market and bring faster pages to local visitors.
    </div>
    <div class="note-soft">Our hosting plans include daily backups, security checks and support from a team that speaks your language.</div>
    <h3>Velmora Outcomes is here to help!</h3>
    <p>We have servers across many regions and can move your site to the location that suits your customers best. Setup is simple and handled fully by our staff.</p>
    <p><b>Contact us about our International Hosting service today!</b></p>
  </div>
  <div class="photo photo-globe" role="img" aria-label="Photo of a globe with network lines" style="left:305px;top:6px;width:290px;height:225px"></div>
  <div class="fact" style="left:0;top:398px;width:295px;height:40px">
    <div class="head">Did you know .....<span>!</span></div>
    <div>Half of online shoppers leave a site that takes over three seconds to load.</div>
  </div>

  <div class="col block" style="left:615px;top:6px;width:280px">
    <h3>Blog</h3>
    <p>You may be asking why we should run our own blog. A regular blog shows customers that you are active and gives search engines fresh content to read.</p>
    <p>The company's content page is one of the most important places to connect with readers. Every new post is a new page that can rank for more keywords.</p>
    <div class="note">
      <b>Why Blog?</b>
      A blog builds trust, answers customer questions and brings new visitors each week.
    </div>
    <div class="note-soft">Our writers create clear articles in fluent English, planned around the terms your buyers search for.</div>
  </div>
  <div class="photo photo-blog" role="img" aria-label="Photo of a person working on a laptop" style="left:905px;top:6px;width:295px;height:225px"></div>
  <div class="col block" style="left:615px;top:245px;width:575px">
    <h3>The Increase Brand Audience</h3>
    <p>A blog shared with your international customers lets them follow your news, new products and offers. Each post can be shared again by readers, spreading your name to people you have never met and building a loyal audience across many countries over time.</p>
    <p><b>Contact us about our Blog Writing Today.</b></p>
  </div>
  <div class="fact" style="left:615px;top:415px;width:280px;height:40px">
    <div class="head">Did you know .....<span>!</span></div>
    <div>Companies that blog receive far more website visitors.</div>
  </div>
</section>

<section class="block" style="left:0;top:1740px;width:1200px;height:455px" aria-label="Logo and website design spread">
  <div class="photo photo-design" role="img" aria-label="Photo of a designer at a desk" style="left:0;top:0;width:295px;height:165px"></div>
  <div class="section-tag" style="left:0;top:55px;width:210px;height:56px;font-size:19px;line-height:1.1">Logo and<br>Website Design</div>

  <div class="col block" style="left:305px;top:4px;width:285px">
    <p>We are all aware that making your business stand out from the crowd is hard if you want to be successful. A strong logo and a modern website make the first impression count.</p>
    <p>Our design team gives you access to hundreds of designers, so you can choose from many ideas rather than one.</p>
    <div class="note">
      <b>Why Velmora Outcomes?</b>
      Through Pixel hive we put your brief in front of a large group of talented designers. You receive many concepts, pick your favourite and only pay for the design you love.
    </div>
    <h3>The Design Process</h3>
    <ol class="steps">
      <li>1. Contact us and tell us what you need.</li>
      <li>2. We prepare a clear brief for the designers.</li>
      <li>3. Designers submit their first concepts.</li>
      <li>4. You give feedback and request changes.</li>
      <li>5. The designers refine their work.</li>
      <li>6. You choose the winner and receive the files.</li>
    </ol>
  </div>
  <div class="fact" style="left:0;top:395px;width:295px;height:42px">
    <div class="head">Did you know .....<span>!</span></div>
    <div>Visitors form an opinion of a website in under one second.</div>
  </div>

  <div class="col block" style="left:615px;top:4px;width:280px">
    <h2>Our Method Vs The Traditional Method</h2>
    <div class="sub">See for yourself</div>
    <h3>Our Method</h3>
    <table class="method">
      <tr class="tall"><th>Cost</th><td>Fixed low price agreed at the start with no hidden charges.</td></tr>
      <tr class="tall"><th>Number of designs</th><td>Dozens of designs to choose from.</td></tr>
      <tr class="tall"><th>Variety of design</th><td>Many styles from designers all over the world.</td></tr>
      <tr class="tall"><th>Number of designers</th><td>Hundreds of skilled designers.</td></tr>
      <tr class="tall"><th>Number of alterations to design</th><td>Unlimited changes during the project.</td></tr>
      <tr class="tall"><th>Timeframe</th><td>About one week from brief to files.</td></tr>
    </table>
  </div>
  <div class="col block" style="left:910px;top:4px;width:280px">
    <h3 style="margin-top:30px">Traditional Method</h3>
    <table class="method">
      <tr class="tall"><th>Cost</th><td>High hourly fees that grow with every extra round of work.</td></tr>
      <tr class="tall"><th>Number of designs</th><td>Usually two or three.</td></tr>
      <tr class="tall"><th>Variety of design</th><td>Limited to one studio style.</td></tr>
      <tr class="tall"><th>Number of designers</th><td>One or two designers.</td></tr>
      <tr class="tall"><th>Number of alterations to design</th><td>Few changes before extra fees apply.</td></tr>
      <tr class="tall"><th>Timeframe</th><td>Several weeks or more.</td></tr>
    </table>
  </div>
  <div class="fact" style="left:615px;top:405px;width:280px;height:40px">
    <div class="head">Did you know .....<span>!</span></div>
    <div>A clear logo helps customers remember your brand.</div>
  </div>
  <div class="fact" style="left:910px;top:405px;width:280px;height:40px">
    <div class="head">Did you know .....<span>!</span></div>
    <div>Most buyers research a company online before calling.</div>
  </div>
</section>

<section class="block dark-band" style="left:0;top:2207px;width:1200px;height:311px" aria-label="Back cover pocket"></section>

</body>
</html>
```